Hollow Lantern Distillery

I need a label designed for my small distillery. I’d like it to have a rose, and the name hollow lantern in script writing. I need the graphic to fit a standard gin bottle and I’ll need to be able to edit it depending on alcohol, warning and descriptions. I want it to look elegant and attractive, but slightly daring too. It’s a 700ml oslo bottle
Target Market(s)
Bespoke gin and vodka drinkers
Industry/Entity Type
Beverage
Font styles to use
Script
Other font styles liked:
- Something easy to read
Requirements
Must have
- Room for me to add and remove text depending on the drink
Nice to have
- Hollow lantern in script, slight colour on the rose and black writing

```html
<!DOCTYPE html>
<html lang="en">
<head>
<meta charset="utf-8">
<title>Hollow Lantern Distillery – Gin Label</title>
<link href="https://fonts.googleapis.com/css2?family=Great+Vibes&family=Kalam:wght@700&family=Libre+Baskerville&display=swap" rel="stylesheet">
<style>
  :root {
    --page: #ffffff;
    --navy-deep: #16233a;
    --navy: #223a57;
    --navy-light: #2c4766;
    --gold: #d9a441;
    --gold-light: #f3d27a;
    --gold-dark: #9c6b1c;
    --rose: #b76f7a;
    --plum: #6b2e5c;
    --petal-white: #e9e6e0;
    --leaf: #56705a;
    --ink: #111111;
    --paper: #f4f4f6;
  }
  * { box-sizing: border-box; margin: 0; padding: 0; }
  html, body {
    width: 900px; height: 1200px; overflow: hidden;
    background: var(--page);
  }
  .canvas { position: relative; width: 900px; height: 1200px; }

  .label {
    position: absolute; left: 60px; top: 94px;
    width: 780px; height: 1010px;
  }
  .label-art { position: absolute; inset: 0; }

  .brand-name {
    position: absolute; left: 40px; top: 290px; width: 706px;
    text-align: center;
    font-family: "Great Vibes", cursive;
    font-size: 118px; line-height: 0.98;
    background: linear-gradient(180deg, var(--gold-light) 0%, var(--gold) 45%, var(--gold-dark) 100%);
    -webkit-background-clip: text; background-clip: text;
    color: transparent;
  }
  .brand-name span { display: block; }
  .brand-name .line-two { margin-left: -20px; }

  .spec-table {
    position: absolute; left: 79px; top: 761px;
    width: 627px; height: 179px;
    background: var(--paper);
    padding: 9px;
  }
  .spec-grid {
    width: 100%; height: 100%;
    border: 3px solid var(--ink);
    display: grid;
    grid-template-rows: 1fr 1fr 1fr;
  }
  .spec-row { display: grid; border-bottom: 1.5px solid var(--ink); }
  .spec-row:last-child { border-bottom: none; }
  .row-cask { grid-template-columns: 130px 185px 1fr; }
  .row-strength { grid-template-columns: 250px 190px 1fr; }
  .row-batch { grid-template-columns: 371px 1fr; }
  .spec-cell {
    display: flex; align-items: center; justify-content: center;
    border-right: 1.5px solid var(--ink);
    font-family: "Kalam", cursive; font-weight: 700;
    font-size: 20px; color: var(--ink);
    transform: skewX(-6deg);
  }
  .spec-cell:last-child { border-right: none; }
  .spec-volume {
    font-family: "Libre Baskerville", serif; font-weight: 400;
    font-size: 27px; transform: none;
  }
  .spec-batch { justify-content: flex-start; padding-left: 10px; gap: 22px; transform: none; }
  .batch-caption { font-family: "Libre Baskerville", serif; font-size: 10px; font-weight: 400; align-self: flex-start; margin-top: 8px; }
  .batch-number { transform: skewX(-6deg); }
</style>
</head>
<body>
<main class="canvas">
  <section class="label" aria-label="Hollow Lantern gin label">
    <svg class="label-art" viewBox="0 0 780 1010" width="780" height="1010" xmlns="http://www.w3.org/2000/svg">
      <defs>
        <linearGradient id="panel-fill" x1="0" y1="0" x2="1" y2="1">
          <stop offset="0" stop-color="var(--navy-deep)"/>
          <stop offset="0.5" stop-color="var(--navy)"/>
          <stop offset="1" stop-color="var(--navy-deep)"/>
        </linearGradient>
        <linearGradient id="diamond-fill" x1="0" y1="0" x2="1" y2="1">
          <stop offset="0" stop-color="var(--navy-deep)"/>
          <stop offset="0.55" stop-color="var(--navy-light)"/>
          <stop offset="1" stop-color="var(--navy)"/>
        </linearGradient>
        <linearGradient id="gold-line" x1="0" y1="0" x2="1" y2="1">
          <stop offset="0" stop-color="var(--gold-light)"/>
          <stop offset="0.5" stop-color="var(--gold)"/>
          <stop offset="1" stop-color="var(--gold-dark)"/>
        </linearGradient>
        <radialGradient id="rose-tone"><stop offset="0" stop-color="var(--rose)"/><stop offset="1" stop-color="var(--rose)" stop-opacity="0"/></radialGradient>
        <radialGradient id="plum-tone"><stop offset="0" stop-color="var(--plum)"/><stop offset="1" stop-color="var(--plum)" stop-opacity="0"/></radialGradient>
        <radialGradient id="white-tone"><stop offset="0" stop-color="var(--petal-white)"/><stop offset="1" stop-color="var(--petal-white)" stop-opacity="0"/></radialGradient>
        <radialGradient id="leaf-tone"><stop offset="0" stop-color="var(--leaf)"/><stop offset="1" stop-color="var(--leaf)" stop-opacity="0"/></radialGradient>
        <linearGradient id="flourish-tone" x1="0" y1="0" x2="1" y2="0">
          <stop offset="0" stop-color="var(--gold)" stop-opacity="0"/>
          <stop offset="0.5" stop-color="var(--gold)"/>
          <stop offset="1" stop-color="var(--gold)" stop-opacity="0"/>
        </linearGradient>
      </defs>

      <rect class="label-panel" x="0" y="0" width="780" height="1010" fill="url(#panel-fill)"/>

      <g class="floral-illustration" role="img" aria-label="Illustrated roses in dusty pink, plum and white with green leaves">
        <ellipse cx="175" cy="140" rx="160" ry="150" fill="url(#rose-tone)"/>
        <ellipse cx="580" cy="70" rx="120" ry="70" fill="url(#white-tone)"/>
        <ellipse cx="690" cy="150" rx="90" ry="80" fill="url(#leaf-tone)"/>
        <ellipse cx="700" cy="380" rx="110" ry="170" fill="url(#plum-tone)"/>
        <ellipse cx="560" cy="640" rx="80" ry="80" fill="url(#white-tone)"/>
        <ellipse cx="700" cy="640" rx="90" ry="150" fill="url(#leaf-tone)"/>
        <ellipse cx="80" cy="620" rx="80" ry="90" fill="url(#leaf-tone)"/>
        <ellipse cx="400" cy="780" rx="260" ry="110" fill="url(#plum-tone)"/>
        <ellipse cx="720" cy="900" rx="70" ry="110" fill="url(#leaf-tone)"/>
      </g>

      <rect class="outer-frame" x="10" y="10" width="760" height="990" fill="none" stroke="url(#gold-line)" stroke-width="4"/>

      <polygon class="title-diamond" points="393,36 746,402 393,768 40,402" fill="url(#diamond-fill)"/>
      <polygon class="diamond-frame" points="393,36 746,402 393,768 40,402" fill="none" stroke="url(#gold-line)" stroke-width="3"/>
      <polygon class="diamond-inner-frame" points="393,50 732,402 393,754 54,402" fill="none" stroke="url(#gold-line)" stroke-width="1.5"/>

      <ellipse class="flourish-top" cx="393" cy="186" rx="100" ry="8" fill="url(#flourish-tone)" role="img" aria-label="Gold scroll flourish"/>
      <ellipse class="flourish-bottom" cx="393" cy="660" rx="100" ry="8" fill="url(#flourish-tone)" role="img" aria-label="Gold scroll flourish"/>
    </svg>

    <h1 class="brand-name"><span class="line-one">Hollow</span><span class="line-two">Lantern</span></h1>

    <div class="spec-table">
      <div class="spec-grid">
        <div class="spec-row row-cask">
          <div class="spec-cell">Single Cask</div>
          <div class="spec-cell">Double Grain</div>
          <div class="spec-cell">One of the 3000 bottles</div>
        </div>
        <div class="spec-row row-strength">
          <div class="spec-cell">Proof 86</div>
          <div class="spec-cell spec-volume">700 ml</div>
          <div class="spec-cell">40% alc.vol.</div>
        </div>
        <div class="spec-row row-batch">
          <div class="spec-cell">Handcrafted</div>
          <div class="spec-cell spec-batch"><span class="batch-caption">BATCH No.</span><span class="batch-number">126 of 3000</span></div>
        </div>
      </div>
    </div>
  </section>
</main>
</body>
</html>
```